Pflegedienst sucht Flyerdesign
Zielgruppe
Wir sind ein ambulanter Pflegedienst und betreuen ca. 200 Patienten in ländlicher Region. Unsere Zielgruppe sind Pflegebedürftige aus altersbedingten Gründen oder nach Krankenhausaufenthalten. Wir setzen auf Qualität, Zuverlässigkeit, Exklusivität.
Aufgabenstellung
DIN lang Flyer. Wir werben ganz bewußt nicht mit Bildern von Senioren oder alten Menschen, weil das fast alle Pflegedienste tun. Daher setzen wir eher auf Motive aus unserer Urlaubsregion: Strand, Meer...
Unseren Firmen-Vebo hätten wir gern als Fotoausschnitt ohne Hintergund mit dabei.
Und einen Kartenausschnitt mit unserem Einzugsgebiet fänden wir toll. Dies umfasst ca. 15 km um Seewinkel und Fördeholm folgende Orte: Stein, Wendtorf, Probsteierhagen, Schönkirchen und Mönkeberg.

```html
<!DOCTYPE html>
<html lang="de">
<head>
<meta charset="utf-8">
<title>Ambulante Krankenpflege Seewinkel – Flyer</title>
<link href="https://fonts.googleapis.com/css2?family=Bitter:wght@400;600;700&display=swap" rel="stylesheet">
<style>
:root{
  --magenta:#ad1f65;
  --magenta-light:#d99ab9;
  --panel-grey:#ebebeb;
  --ink:#1d1d1b;
  --slate:#7f8d92;
  --white:#ffffff;
}
*{margin:0;padding:0;box-sizing:border-box}
html,body{width:1200px;height:848px;overflow:hidden;background:var(--white)}
body{font-family:"Bitter",serif;color:var(--ink);position:relative}
.panel{position:absolute;top:0;height:848px;overflow:hidden}
.panel--contacts{left:0;width:392px;background:var(--panel-grey)}
.panel--address{left:392px;width:404px;background:var(--white)}
.panel--cover{left:796px;width:404px;background:var(--white)}
.abs{position:absolute}
.heading{color:var(--magenta);font-weight:700;line-height:1.2}
.portrait{position:absolute;width:86px;height:90px;border:3px solid var(--white);background:linear-gradient(160deg,#e3d2c6,#b7a091 60%,#5d4d44)}
.person-name{color:var(--magenta);font-weight:700;font-size:14px;line-height:20px}
.person-role{font-size:14px;line-height:20px}
.quote{font-size:13.3px;line-height:20px;width:330px}
.rule{position:absolute;left:33px;width:330px;height:1.5px;background:var(--magenta)}
.call{display:flex;align-items:center;gap:12px}
.call-text{color:var(--magenta);font-weight:700;line-height:28px}
.label{color:var(--magenta);font-size:14px;line-height:21px}
.address-lines{font-size:14px;line-height:21.3px;letter-spacing:.2px}
.service-map{position:absolute;left:24px;top:522px;width:350px;height:66px;border-radius:4px;
  background:linear-gradient(120deg,#cfe0e8 0%,#dfe9d8 55%,#eef0e4 100%)}
.cover-photo{position:absolute;left:0;top:0;width:404px;height:534px;
  background:linear-gradient(180deg,#c8d5e1 0%,#dbe3ea 35%,#a8bfd3 48%,#7f9fbb 56%,#b9b198 66%,#e9ebee 78%,#f2f3f5 100%)}
.badge{position:absolute;left:218px;top:433px;width:144px;height:144px;border-radius:50%;background:var(--magenta-light);display:flex;align-items:center;justify-content:center}
.badge-inner{width:122px;height:122px;border-radius:50%;background:var(--magenta);color:var(--white);font-weight:700;font-size:14.5px;line-height:20px;text-align:center;display:flex;align-items:center;justify-content:center}
.services{list-style:none;font-size:15px;line-height:23px}
.services li{padding-left:13px;position:relative}
.services li::before{content:"";position:absolute;left:1px;top:9px;width:4px;height:4px;background:var(--magenta)}
.brand-name{color:var(--slate);font-weight:400;font-size:17px;line-height:22px;text-align:right}
.vehicle{position:absolute;left:26px;top:604px;width:350px;height:154px;border-radius:70px 90px 30px 30px;background:linear-gradient(180deg,#8b9399,#6a7177 60%,#3f4448)}
</style>
</head>
<body>

<section class="panel panel--contacts">
  <h2 class="heading abs" style="left:32px;top:33px;font-size:23px">Ihre Ansprechpartner:</h2>

  <div class="portrait" style="left:32px;top:69px" role="img" aria-label="Porträtfoto der Geschäftsleitung"></div>
  <div class="abs" style="left:136px;top:69px">
    <div class="person-name">Miriam Hollerbeck</div>
    <div class="person-role">Geschäftsleitung</div>
  </div>
  <p class="quote abs" style="left:32px;top:169px">„Einen ambulanten Pflegedienst in Anspruch zu nehmen, bedeutet im ersten Moment, fremden Menschen zu vertrauen.<br>Deswegen möchten wir uns bei einem Erstgespräch vorstellen und uns gegenseitig kennen lernen. Dabei entwickeln wir mit Ihnen, Ihren Angehörigen und unseren Pflegekräften ein auf Sie abgestimmtes individuelles Versorgungskonzept und beraten Sie natürlich gerne auch zur Finanzierung.“</p>
  <div class="rule" style="top:357px"></div>

  <div class="portrait" style="left:32px;top:369px" role="img" aria-label="Porträtfoto der Pflegedienstleitung"></div>
  <div class="abs" style="left:136px;top:369px">
    <div class="person-name">Anke Sörensen</div>
    <div class="person-role">Pflegedienstleitung Einsatzleitung<br>Fördeholm</div>
  </div>
  <p class="quote abs" style="left:32px;top:468px">„Im Mittelpunkt unserer Bemühungen stehen die Zufriedenheit und die Lebensqualität unserer Patienten. Deswegen begreifen wir unsere Arbeit als einen ständigen Prozess, innerhalb dessen wir die individuelle Situation der Pflegebedürftigen ständig überprüfen, um ihnen die jeweils bestmögliche und auf ihre Bedürfnisse optimal abgestimmte Pflegequalität zukommen lassen zu können.“</p>
  <div class="rule" style="top:639px"></div>

  <div class="portrait" style="left:32px;top:652px" role="img" aria-label="Porträtfoto der stellvertretenden Pflegedienstleitung"></div>
  <div class="abs" style="left:136px;top:648px">
    <div class="person-name">Birte Lammers</div>
    <div class="person-role">Stellv. Pflegedienstleitung Einsatz-<br>leitung Seewinkel</div>
  </div>

  <div class="call abs" style="left:30px;top:762px">
    <svg width="52" height="52" viewBox="0 0 52 52" aria-hidden="true">
      <circle cx="26" cy="26" r="22" fill="none" stroke="var(--magenta)" stroke-width="6"/>
      <path d="M16 14 l6 -2 l4 8 l-4 3 q3 7 9 10 l3 -4 l8 4 l-2 6 q-12 2 -21 -9 q-6 -8 -3 -16z" fill="var(--magenta)"/>
    </svg>
    <div class="call-text" style="font-size:22px">Rufen Sie uns gerne an:<br>04399 - 2140</div>
  </div>
</section>

<section class="panel panel--address">
  <h1 class="heading abs" style="left:24px;top:33px;font-size:23px;line-height:28px">Ambulante Krankenpflege<br>Seewinkel GmbH</h1>
  <div class="abs" style="left:24px;top:112px">
    <div class="label">Hauptsitz:</div>
    <div class="address-lines">Dünenweg 7<br>24199 Seewinkel<br>TEL 04399 – 21 40<br>FAX 04399 – 21 49<br><br>info@pflege-seewinkel.de<br>www.pflege-seewinkel.de</div>
    <div class="label" style="margin-top:21px">Niederlassung:</div>
    <div class="address-lines">Hafenstieg 4<br>24198 Fördeholm<br>TEL 0439 – 47 32 18 60<br>FAX 0439 – 47 32 18 61</div>
  </div>
  <div class="call abs" style="left:24px;top:450px">
    <svg width="52" height="52" viewBox="0 0 52 52" aria-hidden="true">
      <circle cx="26" cy="26" r="22" fill="none" stroke="var(--magenta)" stroke-width="6"/>
      <path d="M16 14 l6 -2 l4 8 l-4 3 q3 7 9 10 l3 -4 l8 4 l-2 6 q-12 2 -21 -9 q-6 -8 -3 -16z" fill="var(--magenta)"/>
    </svg>
    <div class="call-text" style="font-size:22px;letter-spacing:.5px">Rufbereitschaft<br><span style="font-size:23px">0170 – 98 76 512</span></div>
  </div>
  <div class="service-map" role="img" aria-label="Kartenausschnitt des Einzugsgebiets rund 15 km um Seewinkel und Fördeholm"></div>
  <div class="vehicle" role="img" aria-label="Freigestelltes Foto des grauen Vebo-Firmenwagens mit Beschriftung"></div>
</section>

<section class="panel panel--cover">
  <div class="cover-photo" role="img" aria-label="Winterlicher Strand mit Dünengras, Meer und Küstenort im Hintergrund"></div>
  <svg class="abs" style="left:0;top:440px" width="404" height="95" viewBox="0 0 404 95" aria-hidden="true">
    <path d="M0 75 Q200 70 404 30 L404 95 L0 95Z" fill="var(--magenta)"/>
  </svg>
  <div class="abs" style="left:33px;top:40px">
    <div style="color:var(--magenta);font-size:19.5px;line-height:25px">Ambulante Krankenpflege<br>Seewinkel &amp; Fördeholm</div>
    <div class="heading" style="font-size:35px;line-height:37px;margin-top:8px">Ihr Premiumdienst<br>in der Region</div>
  </div>
  <div class="badge"><div class="badge-inner">Von<br>Mensch zu<br>Mensch seit<br>über 20<br>Jahren</div></div>
  <ul class="services abs" style="left:20px;top:568px">
    <li>Häusliche Pflege</li>
    <li>Pflegeberatung</li>
    <li>Demenzbetreuung</li>
    <li>Aktivierende Beschäftigung</li>
    <li>Entlastung im Haushalt</li>
    <li style="margin-top:3px">Palliativpflege Sterbebegleitung<br>24 h Rufbereitschaft</li>
  </ul>
  <div class="brand-name abs" style="right:44px;top:782px">Pflegedienst Seewinkel &amp; Fördeholm</div>
</section>

</body>
</html>
```